Powerpoint design template for PLAYNOVA for new digital platform

We would like to use a PowerPoint template, we would like to create a new page, we would like to create a new digital platform PLAYNOVA for schools and parents for the creation of playful communication and educational tools for children to enhance their positive development, amaze them learn in a playful way. This platform is going to be the most creative, stimulating and innovative classroom, easy to use and fast to implement. Scrapbooking, collages ... Magazine, newsletters Diplomla / awards Slideshows Facebook Calendars Organizers Greetings Games ... This powerpoint template will be used essential to We are looking for a professional design, positioning our brand in the children market with an adult hearing. so you will need to find a good deal. Primary target: nurseries & schools from 0 to 18 years old and universities (in 2nd phase) Secondary target: small & medium businesses Third target: general public, and TPE If it is a color scheme, then it is suggested that it be marketed in Europe (UK, Italy, Spain) and in a 2nd Stage USA and other countries. multiple options for front page, insidious pages (multiple styles with limited text and extended text) and final contact page We need something to read, we can not do it too much, but we can not do it. , and inside pages aligned to our logo

Target Market(s)

Target 1; Education with teacher Target 2; parents and grandparents

Industry/Entity Type

Education

Font styles to use
Other font styles liked:
• not decided. but not too fancy

Requirements
Must have
• Multi page options for front page, page insides (multiple styles with limited text and extended text) and final page contact
Nice to have
• do not have a lot of ideas. We need something to read, we can not get away from it
Should not have
• not too fancy and busy: keep clarity & simplicity while reassuring on quality

```html
<!DOCTYPE html>
<html lang="en">
<head>
<meta charset="utf-8">
<title>PLAYNOVA – Presentation Template</title>
<link rel="stylesheet" href="https://fonts.googleapis.com/css2?family=Roboto+Condensed:wght@400;700&family=Roboto:wght@400;500;700&display=swap">
<style>
:root{
  --lime:#cddc39;
  --lime-dark:#b5c72a;
  --orange:#f7941d;
  --blue:#1aa9e5;
  --pink:#e8297f;
  --purple:#7b2d6b;
  --red:#e31e24;
  --yellow:#fbb817;
  --teal:#34d3bd;
  --green:#8cc63f;
  --ink:#333;
  --muted:#777;
  --pale:#fbf7c4;
  --bg:#000;
}
*{margin:0;padding:0;box-sizing:border-box}
html,body{width:1200px;height:891px;overflow:hidden;background:var(--bg)}
body{position:relative;font-family:"Roboto",Arial,sans-serif;color:var(--ink)}
.slide{position:absolute;width:366px;height:275px;overflow:hidden;background:#fff}
.c1{left:21px}.c2{left:414px}.c3{left:807px}
.r1{top:15px}.r2{top:308px}.r3{top:596px}
.abs{position:absolute}
.brand{font-family:"Roboto Condensed",Arial,sans-serif;font-weight:700;color:var(--purple);letter-spacing:.5px}
.brand-sm{font-size:11px}
.title{font-family:"Roboto Condensed",Arial,sans-serif;font-weight:700}
/* header */
.hdr{position:absolute;left:0;top:0;width:366px;height:33px;background:var(--lime)}
.hdr .title{position:absolute;left:10px;top:8px;font-size:16px;color:var(--ink)}
.hdr svg{position:absolute;right:0;top:0}
.hdr .brand{position:absolute;right:14px;top:11px}
.hdr-white{position:absolute;left:0;top:0;width:366px;height:40px;background:#fff}
.hdr-white .title{position:absolute;left:12px;top:12px;font-size:14px;color:var(--pink);font-weight:400}
.hdr-white .brand{position:absolute;right:14px;top:13px}
/* footer */
.ftr{position:absolute;left:0;bottom:0;width:366px;height:20px;background:var(--lime)}
.ftr .url{position:absolute;left:7px;top:5px;font-family:"Roboto Condensed",sans-serif;font-size:8px;color:var(--ink)}
.ftr svg{position:absolute;right:0;top:0}
.ftr .page{position:absolute;right:10px;top:5px;font-family:"Roboto Condensed",sans-serif;font-size:8px;color:var(--ink)}
p.body{font-size:6.6px;line-height:1.6;color:var(--muted)}
/* slide 1 */
.cover .name{left:16px;top:98px;font-size:27px}
.cover .ptitle{left:16px;top:138px;font-size:15px;color:#4a4a4a;font-weight:400;letter-spacing:.6px}
.cover .sub{left:16px;top:160px;font-size:8px;font-weight:500}
.cover .badge-name{left:198px;top:198px;font-size:22px}
.cover .tag{left:200px;top:226px;font-size:6px;letter-spacing:2px;color:#555;line-height:1.4}
/* slide 2 */
.band{position:absolute;left:0;width:366px;color:#fff}
.band .num{position:absolute;left:8px;top:2px;font-family:"Roboto Condensed",sans-serif;font-weight:700;font-size:44px;color:rgba(255,255,255,.55)}
.band h3{position:absolute;left:42px;top:6px;font-size:10.5px;font-weight:500}
.band p{position:absolute;left:42px;top:22px;width:318px;font-size:6.5px;line-height:1.65;color:rgba(255,255,255,.9)}
/* slide 3 & 5 items */
.item{position:absolute}
.item .st{font-size:9px;font-weight:500}
.book{position:absolute;width:10px;height:13px;border-radius:1px;transform:rotate(-20deg)}
.photo{position:absolute}
/* table */
.tbl{position:absolute;left:12px;top:92px;border-collapse:collapse;width:342px}
.tbl th{height:36px;font-size:5.5px;color:#fff;font-weight:500;vertical-align:bottom;padding-bottom:5px}
.tbl th.lbl{color:var(--ink);font-size:8px;text-align:center;font-weight:700;vertical-align:middle;padding:0}
.tbl td{height:24px;text-align:center;font-size:6.5px;color:#888}
.tbl tr:nth-child(odd) td{background:#f0f0f0}
.tbl td.lbl{text-align:left;padding-left:10px;background:#e4e4e4 !important}
.tick{display:inline-block;width:9px;height:9px;border-radius:2px;vertical-align:middle}
.ico{display:block;margin:0 auto 3px}
/* features grid */
.feat{position:absolute;width:112px}
.feat .dot{position:absolute;left:6px;top:0;width:22px;height:22px;border-radius:50%}
.feat .lab{position:absolute;left:32px;top:7px;font-size:6.8px}
.feat p{position:absolute;left:0;top:30px;width:112px;font-size:6px;line-height:1.75;color:#999;text-align:justify}
/* strategy rows */
.strat{position:absolute;left:0;width:366px;height:40px}
.strat svg{position:absolute;left:0;top:0}
.strat h4{position:absolute;left:62px;top:0;font-size:7px;font-weight:500}
.strat p{position:absolute;left:62px;top:11px;width:295px;font-size:4.8px;line-height:1.55;color:#888}
/* quadrants */
.quad{position:absolute;width:181px;height:116px;color:#fff}
.quad h3{position:absolute;left:11px;top:30px;font-size:10.5px;font-weight:500}
.quad p{position:absolute;left:11px;top:46px;width:164px;font-size:6.6px;line-height:1.7;color:rgba(255,255,255,.92)}
.numdot{position:absolute;width:17px;height:17px;border-radius:50%;background:#fff;border:2px solid currentColor;font-size:9px;font-weight:700;text-align:center;line-height:13px}
</style>
</head>
<body>

<!-- Slide 1: cover -->
<section class="slide c1 r1 cover">
  <svg class="abs" style="left:0;top:0" width="366" height="275" viewBox="0 0 366 275">
    <polygon points="0,0 350,0 88,275 0,275" fill="var(--lime)"/>
    <polygon points="305,0 366,0 366,20 110,275 70,275" fill="#fff" opacity=".9"/>
    <polygon points="340,10 366,10 366,30 120,275 100,275" fill="var(--lime-dark)" opacity=".5"/>
    <polygon points="0,0 366,0 366,255 100,275 0,275" fill="none"/>
    <polygon points="210,168 310,168 356,212 300,258 190,258 160,212" fill="var(--lime)"/>
  </svg>
  <div class="abs brand name">PLAYNOVA</div>
  <div class="abs title ptitle">PROJECT TITLE HERE</div>
  <div class="abs title sub">SUBTEXT HERE</div>
  <div class="abs brand badge-name">PLAYNOVA</div>
  <div class="abs tag">YOUR TAGLINE<br>GOES HERE</div>
</section>

<!-- Slide 2: content bands -->
<section class="slide c2 r1">
  <div class="hdr-white"><span class="title">CONTENT TITLE HERE</span><span class="brand brand-sm">PLAYNOVA</span></div>
  <div class="band" style="top:41px;height:76px;background:var(--blue)">
    <span class="num">1</span><h3>Section Title Here</h3>
    <p>Lemon drops oat cake oat cake sugar plum sweet gingerbread chocolate cake gingerbread. Lemon drops oat cake oat cake sugar plum sweet Lemon drops oat cake oat cake sugar plum sweet gingerbread chocolate gingerbread. Lemon drops oat cake oat cake sugar plum sweet</p>
  </div>
  <div class="band" style="top:119px;height:76px;background:var(--orange)">
    <span class="num">2</span><h3>Section Title Here</h3>
    <p>Lemon drops oat cake oat cake sugar plum sweet gingerbread chocolate cake gingerbread. Lemon drops oat cake oat cake sugar plum sweet Lemon drops oat cake oat cake sugar plum sweet gingerbread chocolate gingerbread. Lemon drops oat cake oat cake sugar plum sweet</p>
  </div>
  <div class="band" style="top:197px;height:78px;background:var(--lime)">
    <span class="num">3</span><h3>Section Title Here</h3>
    <p>Lemon drops oat cake oat cake sugar plum sweet gingerbread chocolate cake gingerbread. Lemon drops oat cake oat cake sugar plum sweet Lemon drops oat cake oat cake sugar plum sweet gingerbread chocolate gingerbread. Lemon drops oat cake oat cake sugar plum sweet</p>
  </div>
</section>

<!-- Slide 3: text with photo -->
<section class="slide c3 r1">
  <div class="hdr"><span class="title">PROJECT TITLE HERE</span>
    <svg width="100" height="33"><polygon points="20,0 100,0 100,33 0,33" fill="#fff"/></svg>
    <span class="brand brand-sm">PLAYNOVA</span></div>
  <span class="book" style="left:20px;top:57px;background:var(--purple)"></span>
  <div class="item" style="left:41px;top:56px;width:155px">
    <div class="st" style="color:var(--yellow)">Subtext here</div>
    <p class="body" style="margin-top:2px">Lemon drops oat cake oat cake sugar plum sweet gingerbread chocolate cake ginger-bread. Lemon drops oat cake oat cake sugar plum sweet Lemon drops oat cake oat cake sugar plum sweet gingerbread chocolate cake gingerbread. Lemon drops oat cake oat cake sugar plum sweet</p>
    <p class="body" style="margin-top:8px">Lemon drops oat cake oat cake sugar plum sweet gingerbread chocolate cake ginger-bread. Lemon drops oat cake oat cake sugar plum sweet</p>
  </div>
  <div class="photo" role="img" aria-label="Photo of a smiling child holding up a hand covered in bright paint" style="left:205px;top:55px;width:161px;height:180px;background:radial-gradient(ellipse at 70% 45%,#f1d9c6 0%,#e7c1a4 35%,#f6f1ec 75%,#fff 100%)"></div>
  <div class="ftr"><span class="url">www.playnova.com</span>
    <svg width="70" height="20"><polygon points="0,0 70,0 70,20 18,20" fill="var(--orange)"/></svg>
    <span class="page">Page : 01</span></div>
</section>

<!-- Slide 4: feature table -->
<section class="slide c1 r2">
  <div class="hdr"><span class="title">PROJECT TITLE HERE</span>
    <svg width="100" height="33"><polygon points="20,0 100,0 100,33 0,33" fill="#fff"/></svg>
    <span class="brand brand-sm">PLAYNOVA</span></div>
  <div class="abs" style="left:10px;top:53px;font-size:8px;font-weight:700;color:var(--red)">Subtitle here</div>
  <p class="abs" style="left:10px;top:64px;width:350px;font-size:5.6px;line-height:1.7;color:#555">Liquorice chupa chups applicake apple pie cupcake brownie bear claw cake gingerbread cotton candy. Bear claw croissant apple pie. Croissant cake sweet puff oreo. Liquorice chupa chups applicake apple pie cupcake brownie</p>
  <table class="tbl">
    <tr>
      <th class="lbl" style="width:66px;background:#fff">Special<br>Feature</th>
      <th style="background:var(--red)"><svg class="ico" width="11" height="10"><rect x="1" y="1" width="9" height="6" fill="none" stroke="#fff" stroke-width="1.3"/><rect x="3" y="8" width="5" height="1.3" fill="#fff"/></svg>Version One</th>
      <th style="background:var(--purple)"><svg class="ico" width="11" height="11"><circle cx="5.5" cy="5.5" r="4.3" fill="none" stroke="#fff" stroke-width="1.3"/><circle cx="5.5" cy="5.5" r="1.8" fill="none" stroke="#fff"/></svg>Version Two</th>
      <th style="background:var(--blue)"><svg class="ico" width="11" height="10"><rect x="1" y="1" width="4" height="4" fill="#fff"/><rect x="6" y="1" width="4" height="4" fill="#fff"/><rect x="3" y="5" width="2" height="3" fill="#fff"/><rect x="8" y="5" width="2" height="3" fill="#fff"/></svg>Version Three</th>
      <th style="background:var(--green)"><svg class="ico" width="11" height="11"><polygon points="10,1 1,6 4,7 6,10" fill="#fff"/></svg>Version Four</th>
    </tr>
    <tr><td class="lbl">Feature A</td><td><span class="tick" style="background:var(--red)"></span></td><td><span class="tick" style="background:var(--purple)"></span></td><td><span class="tick" style="background:var(--blue)"></span></td><td><span class="tick" style="background:var(--green)"></span></td></tr>
    <tr><td class="lbl">Feature B</td><td><span class="tick" style="background:var(--red)"></span></td><td><span class="tick" style="background:var(--purple)"></span></td><td><span class="tick" style="background:var(--blue)"></span></td><td><span class="tick" style="background:var(--green)"></span></td></tr>
    <tr><td class="lbl">Feature C</td><td></td><td><span class="tick" style="background:var(--purple)"></span></td><td><span class="tick" style="background:var(--blue)"></span></td><td><span class="tick" style="background:var(--green)"></span></td></tr>
    <tr><td class="lbl">Feature D</td><td></td><td></td><td><span class="tick" style="background:var(--blue)"></span></td><td><span class="tick" style="background:var(--green)"></span></td></tr>
    <tr><td class="lbl">Feature E</td><td></td><td></td><td></td><td><span class="tick" style="background:var(--green)"></span></td></tr>
  </table>
  <div class="ftr"><span class="url">www.playnova.com</span>
    <svg width="70" height="20"><polygon points="0,0 70,0 70,20 18,20" fill="var(--orange)"/></svg>
    <span class="page">Page : 01</span></div>
</section>

<!-- Slide 5: three subtexts -->
<section class="slide c2 r2" style="background:var(--pale)">
  <div class="hdr"><span class="title">PROJECT TITLE HERE</span>
    <svg width="100" height="33"><polygon points="20,0 100,0 100,33 0,33" fill="#fff"/></svg>
    <span class="brand brand-sm">PLAYNOVA</span></div>
  <span class="book" style="left:20px;top:80px;background:var(--purple)"></span>
  <div class="item" style="left:47px;top:77px;width:300px"><div class="st" style="color:var(--yellow)">Subtext here</div><p class="body" style="font-size:7.6px;line-height:1.5;color:#666">Lemon drops oat cake oat cake sugar plum sweet gingerbread chocolate cake gingerbread. Lemon drops oat cake oat cake sugar plum sweet</p></div>
  <span class="book" style="left:20px;top:125px;background:var(--pink)"></span>
  <div class="item" style="left:47px;top:122px;width:300px"><div class="st" style="color:var(--pink)">Subtext here</div><p class="body" style="font-size:7.6px;line-height:1.5;color:#666">Lemon drops oat cake oat cake sugar plum sweet gingerbread chocolate cake gingerbread. Lemon drops oat cake oat cake sugar plum sweet</p></div>
  <span class="book" style="left:20px;top:167px;background:#2b6b73"></span>
  <div class="item" style="left:47px;top:164px;width:300px"><div class="st" style="color:#2b8a96">Subtext here</div><p class="body" style="font-size:7.6px;line-height:1.5;color:#666">Lemon drops oat cake oat cake sugar plum sweet gingerbread chocolate cake gingerbread. Lemon drops oat cake oat cake sugar plum sweet</p></div>
  <div class="ftr"><span class="url">www.playnova.com</span>
    <svg width="70" height="20"><polygon points="0,0 70,0 70,20 18,20" fill="var(--orange)"/></svg>
    <span class="page">Page : 01</span></div>
</section>

<!-- Slide 6: section divider -->
<section class="slide c3 r2">
  <div class="photo" role="img" aria-label="Soft faded photo of smiling schoolchildren at a classroom table" style="left:0;top:0;width:366px;height:275px;background:linear-gradient(180deg,#eef3f6 0%,#f4ece6 45%,#f6f1e2 75%,#eef1ec 100%)"></div>
  <div class="abs brand brand-sm" style="right:14px;top:11px">PLAYNOVA</div>
  <div class="abs title" style="left:0;width:366px;top:113px;text-align:center;font-size:22px;color:var(--blue);letter-spacing:.3px">SECTION TITLE HERE</div>
  <p class="abs" style="left:30px;width:306px;top:143px;text-align:center;font-size:7.4px;line-height:1.5;color:#333">Bear claw croissant apple pie. Croissant cake tart liquorice tart pastry. Tiramisu apple pie biscuit sweet oat cake sweet icing brownie.</p>
  <div class="ftr"><span class="url">www.playnova.com</span>
    <svg width="70" height="20"><polygon points="0,0 70,0 70,20 18,20" fill="var(--orange)"/></svg>
    <span class="page">Page : 01</span></div>
</section>

<!-- Slide 7: feature grid -->
<section class="slide c1 r3">
  <div class="hdr"><span class="title">PROJECT TITLE HERE</span>
    <svg width="100" height="33"><polygon points="20,0 100,0 100,33 0,33" fill="#fff"/></svg>
    <span class="brand brand-sm">PLAYNOVA</span></div>
  <div class="feat" style="left:13px;top:66px"><span class="dot" style="background:var(--red)"></span><span class="lab" style="color:var(--red)">Creative Strategy</span><p>Liquorice chupa chups applicake apple pie cake cupcake brownie bear claw cake gingerbread cotton candy.</p></div>
  <div class="feat" style="left:137px;top:66px"><span class="dot" style="background:var(--yellow)"></span><span class="lab" style="color:var(--yellow)">Employee Desktop</span><p>Liquorice chupa chups applicake apple pie cake cupcake brownie bear claw cake gingerbread cotton candy.</p></div>
  <div class="feat" style="left:257px;top:66px"><span class="dot" style="background:var(--purple)"></span><span class="lab" style="color:var(--purple)">Business Plan</span><p>Liquorice chupa chups applicake apple pie cake cupcake brownie bear claw cake gingerbread cotton candy.</p></div>
  <div class="feat" style="left:13px;top:162px"><span class="dot" style="background:var(--orange)"></span><span class="lab" style="color:var(--red)">System Protection</span><p>Liquorice chupa chups applicake apple pie cake cupcake brownie bear claw cake gingerbread cotton candy.</p></div>
  <div class="feat" style="left:137px;top:162px"><span class="dot" style="background:var(--green)"></span><span class="lab" style="color:var(--green)">Fun Games</span><p>Liquorice chupa chups applicake apple pie cake cupcake brownie bear claw cake gingerbread cotton candy.</p></div>
  <div class="feat" style="left:257px;top:162px"><span class="dot" style="background:var(--blue)"></span><span class="lab" style="color:var(--blue)">Data Analysis</span><p>Liquorice chupa chups applicake apple pie cake cupcake brownie bear claw cake gingerbread cotton candy.</p></div>
  <div class="ftr"><span class="url">www.playnova.com</span>
    <svg width="70" height="20"><polygon points="0,0 70,0 70,20 18,20" fill="var(--orange)"/></svg>
    <span class="page">Page : 01</span></div>
</section>

<!-- Slide 8: strategy list -->
<section class="slide c2 r3">
  <div class="hdr"><span class="title">PROJECT TITLE HERE</span>
    <svg width="100" height="33"><polygon points="20,0 100,0 100,33 0,33" fill="#fff"/></svg>
    <span class="brand brand-sm">PLAYNOVA</span></div>
  <div class="strat" style="top:56px"><svg width="56" height="34"><polygon points="0,0 46,0 54,17 46,34 0,34" fill="var(--blue)"/><rect x="18" y="10" width="14" height="9" fill="none" stroke="#fff" stroke-width="2"/><rect x="21" y="21" width="8" height="2" fill="#fff"/></svg><h4>Creative Strategy</h4><p>Toffee caramels candy canes bonbon soufflé wafer topping. I love halvah and jujubes lemon drops. Jelly pie chocolate bar biscuit oat cake carrot cake muffin jelly beans chocolate. Sugar plum marshmallow oreo cake cookies topping jelly gummies.</p></div>
  <div class="strat" style="top:102px"><svg width="56" height="34"><polygon points="0,0 46,0 54,17 46,34 0,34" fill="#d629b8"/><polygon points="33,9 19,18 23,20 25,25" fill="#fff"/></svg><h4>Boost Sales</h4><p>Toffee caramels candy canes bonbon soufflé wafer topping. I love halvah and jujubes lemon drops. Jelly pie chocolate bar biscuit oat cake carrot cake muffin jelly beans chocolate. Sugar plum marshmallow oreo cake cookies topping jelly gummies.</p></div>
  <div class="strat" style="top:148px"><svg width="56" height="34"><polygon points="0,0 46,0 54,17 46,34 0,34" fill="var(--yellow)"/><rect x="18" y="11" width="6" height="6" fill="#fff"/><rect x="26" y="11" width="6" height="6" fill="#fff"/><rect x="21" y="17" width="3" height="5" fill="#fff"/><rect x="29" y="17" width="3" height="5" fill="#fff"/></svg><h4>Global Brand Strategy</h4><p>Toffee caramels candy canes bonbon soufflé wafer topping. I love halvah and jujubes lemon drops. Jelly pie chocolate bar biscuit oat cake carrot cake muffin jelly beans chocolate. Sugar plum marshmallow oreo cake cookies topping jelly gummies.</p></div>
  <div class="strat" style="top:194px"><svg width="56" height="34"><polygon points="0,0 46,0 54,17 46,34 0,34" fill="var(--teal)"/><path d="M19 10h12v7c0 4-6 7-6 7s-6-3-6-7z" fill="#fff"/></svg><h4>Business Strategy</h4><p>Toffee caramels candy canes bonbon soufflé wafer topping. I love halvah and jujubes lemon drops. Jelly pie chocolate bar biscuit oat cake carrot cake muffin jelly beans chocolate. Sugar plum marshmallow oreo cake cookies topping jelly gummies.</p></div>
  <div class="ftr"><span class="url">www.playnova.com</span>
    <svg width="70" height="20"><polygon points="0,0 70,0 70,20 18,20" fill="var(--orange)"/></svg>
    <span class="page">Page : 01</span></div>
</section>

<!-- Slide 9: four quadrants -->
<section class="slide c3 r3">
  <div class="hdr-white"><span class="title">CONTENT TITLE HERE</span><span class="brand brand-sm">PLAYNOVA</span></div>
  <div class="quad" style="left:0;top:39px;background:var(--blue)"><h3>Section Title Here</h3><p>Lemon drops oat cake oat cake sugar plum sweet gingerbread chocolate cake gingerbread. Lemon drops oat cake oat cake sugar plum sweet Lemon drops oat cake oat cake sugar plum sweet gingerbread chocolate</p></div>
  <div class="quad" style="left:185px;top:39px;background:var(--pink)"><h3>Section Title Here</h3><p>Lemon drops oat cake oat cake sugar plum sweet gingerbread chocolate cake gingerbread. Lemon drops oat cake oat cake sugar plum sweet Lemon drops oat cake oat cake sugar plum sweet gingerbread chocolate</p></div>
  <div class="quad" style="left:0;top:159px;background:var(--orange)"><h3>Section Title Here</h3><p>Lemon drops oat cake oat cake sugar plum sweet gingerbread chocolate cake gingerbread. Lemon drops oat cake oat cake sugar plum sweet Lemon drops oat cake oat cake sugar plum sweet gingerbread chocolate</p></div>
  <div class="quad" style="left:185px;top:159px;background:var(--yellow)"><h3>Section Title Here</h3><p>Lemon drops oat cake oat cake sugar plum sweet gingerbread chocolate cake gingerbread. Lemon drops oat cake oat cake sugar plum sweet Lemon drops oat cake oat cake sugar plum sweet gingerbread chocolate</p></div>
  <span class="numdot" style="left:74px;top:31px;color:var(--blue)">1</span>
  <span class="numdot" style="left:265px;top:31px;color:var(--pink)">2</span>
  <span class="numdot" style="left:74px;top:151px;color:var(--orange)">3</span>
  <span class="numdot" style="left:265px;top:151px;color:var(--yellow)">4</span>
</section>

</body>
</html>
```